Vormace

I need a professional web site that is directed at the energy industry, Oil, Gas, Mining
I need the website to have the usual pages
1. home page
2. news page.
3. contact us page
4. About us
and a CMS admin section to add further pages and content
Must be Google friendly with SEO facility

Target Market(s)

energy industry, Oil, Gas, Mining

Industry/Entity Type

Industry

Font styles to use
Sans Serif

Colors
faa54b
85cae6
cadf82

Requirements
Must have
• social media icons
site map

```html
<!DOCTYPE html>
<html lang="en">
<head>
<meta charset="utf-8">
<title>Vormace – Energy, Oil, Gas &amp; Mining</title>
<link rel="stylesheet" href="https://fonts.googleapis.com/css2?family=Play:wght@400;700&family=Open+Sans:ital,wght@0,400;0,600;0,700;1,400&display=swap">
<style>
:root{
  --orange:#f7931e;
  --green:#8db33a;
  --ink:#2b2b2b;
  --text:#555;
  --muted:#8a8a8a;
  --dark:#353535;
  --darker:#262626;
  --footer-text:#9a9a9a;
  --white:#fff;
  --head:"Play",sans-serif;
  --body:"Open Sans",sans-serif;
}
*{box-sizing:border-box;margin:0;padding:0}
html,body{width:1200px;height:2261px;overflow:hidden}
body{font-family:var(--body);color:var(--text);background:var(--white);position:relative}
ul{list-style:none}
.wrap{position:relative;width:936px;margin:0 auto}

/* header */
.site-header{height:90px;position:relative}
.brand{position:absolute;left:132px;top:36px;display:flex;align-items:center;gap:8px;font-family:var(--head);font-weight:700;font-size:32px;letter-spacing:2px;color:var(--ink)}
.brand-dot{width:14px;height:14px;border-radius:50%;background:var(--orange)}
.topbar{position:absolute;right:132px;top:14px;display:flex;align-items:center;gap:6px;font-size:13px;color:var(--ink)}
.topbar svg{margin-right:2px}
.social{display:flex;gap:5px}
.social span{display:block;border-radius:50%;background:#888}
.topbar .social{margin-left:8px}
.topbar .social span{width:20px;height:20px}
.main-nav{position:absolute;right:132px;top:62px;display:flex;gap:24px;font-size:12.5px;color:var(--ink);text-transform:uppercase}

/* hero */
.hero{height:373px;position:relative;background:linear-gradient(180deg,#6e6e6e 0%,#8a8a88 40%,#5c5a56 75%,#3d3c3a 100%);text-align:center}
.hero-photo{position:absolute;inset:0;background:radial-gradient(ellipse at 50% 35%,rgba(230,170,40,.35),transparent 60%)}
.hero-title{position:absolute;left:0;right:0;top:196px;font-family:var(--head);font-weight:700;color:var(--orange);text-transform:uppercase;line-height:1.15}
.hero-title .l1{display:block;font-size:25px}
.hero-title .l2{display:block;font-size:33px}
.btn{display:inline-block;background:var(--green);color:var(--white);font-family:var(--head);text-transform:uppercase;text-align:center}
.hero .btn{position:absolute;left:532px;top:280px;width:136px;height:34px;line-height:34px;font-size:15px}
.dots{position:absolute;left:0;right:0;top:343px;display:flex;justify-content:center;gap:6px}
.dots span{width:9px;height:9px;border-radius:50%;background:#ddd}
.dots span:first-child{background:var(--orange)}

/* section headings */
.section-head{text-align:center}
.section-head h2{font-family:var(--head);font-weight:400;font-size:25px;color:var(--ink);text-transform:uppercase}
.section-head p{font-size:15px;color:var(--orange);margin-top:4px}

/* welcome */
.welcome{height:398px;padding-top:38px}
.welcome-body{display:flex;gap:24px;margin-top:26px}
.welcome-photo{width:377px;height:249px;flex:none;background:radial-gradient(ellipse at 55% 45%,#d8a23a 0%,#7a5a22 35%,#1c1a18 75%)}
.welcome-text{font-size:12.5px;line-height:1.55;color:#666}
.welcome-text p{margin-bottom:13px}
.bullets li{position:relative;padding-left:18px;margin-bottom:5.5px}
.bullets li::before{content:"";position:absolute;left:2px;top:7px;width:7px;height:7px;border-radius:50%;background:var(--green)}

/* services */
.services-head{height:87px;padding-top:18px}
.services{height:393px;background:var(--dark);position:relative}
.services::before{content:"";position:absolute;left:581px;top:0;border-left:19px solid transparent;border-right:19px solid transparent;border-top:19px solid var(--white)}
.service-cards{display:flex;gap:24px;padding-top:45px}
.service-card{width:296px;height:311px;background:var(--white);text-align:center}
.service-photo{height:167px}
.service-card h3{font-family:var(--head);font-size:20px;color:var(--ink);margin-top:13px;text-transform:uppercase}
.service-card p{font-size:12.5px;line-height:1.5;color:#444;padding:0 12px;margin-top:3px}
.service-card .btn{font-family:var(--body);text-transform:none;font-size:13px;width:88px;height:29px;line-height:29px;margin-top:16px}
.photo-mining{background:linear-gradient(135deg,#2a2a2a,#8a8c90 55%,#3a3a3a)}
.photo-oil{background:linear-gradient(180deg,#6fa6d6 0%,#9ac1e0 45%,#c06a32 70%,#3b3f55 100%)}
.photo-gas{background:linear-gradient(180deg,#5d9fd2 0%,#9ec2db 45%,#a08a6a 100%)}

/* news */
.news{height:481px;position:relative;background:linear-gradient(180deg,#fff 0%,#f1f2f3 100%);padding-top:42px}
.news-grid{display:flex;gap:24px;margin-top:30px}
.news-card{position:relative;width:456px;height:226px;background:var(--white);box-shadow:0 0 8px rgba(0,0,0,.12)}
.news-photo{position:absolute;left:22px;top:24px;width:194px;height:145px}
.news-date{position:absolute;left:22px;top:24px;width:40px;height:75px;background:var(--green);color:var(--white);text-align:center;font-size:10px;line-height:1.2;padding-top:6px}
.news-date b{display:block;font-size:21px;line-height:1.1}
.news-body{position:absolute;left:230px;top:24px;right:12px}
.news-body h3{font-size:13.5px;font-weight:600;line-height:1.45;color:var(--ink)}
.news-meta{font-size:10px;color:var(--muted);margin-top:4px}
.news-body .excerpt{font-size:11.5px;line-height:1.5;color:#666;margin-top:3px}
.share{position:absolute;left:22px;top:182px;display:flex;gap:7px}
.share span{width:26px;height:26px;background:#d3d3d3}
.read-more{position:absolute;right:22px;top:182px;width:111px;height:27px;line-height:27px;background:var(--orange);color:var(--white);font-size:11.5px;text-align:center}
.news .view-all{display:block;margin:38px auto 0;width:296px;height:41px;line-height:41px;font-size:14px}
.photo-rig{background:linear-gradient(180deg,#c9a33b 0%,#7aa6c8 45%,#2d5d8f 100%)}
.photo-worker{background:linear-gradient(135deg,#3a3630,#9a6a3a 50%,#2a2724)}

/* newsletter */
.newsletter{height:113px;background:var(--orange);color:var(--white)}
.newsletter .wrap{display:flex;align-items:center;height:113px}
.newsletter-copy{width:358px;flex:none;white-space:nowrap}
.newsletter-copy h2{font-size:20px;font-weight:400;line-height:1.25}
.newsletter-copy h2 em{font-family:var(--body)}
.newsletter-copy h2 b{font-weight:700}
.newsletter-copy p{font-size:12.5px}
.field{width:220px;height:32px;flex:none;background:var(--white);color:#888;font-size:12px;line-height:32px;padding-left:12px;margin-right:12px}
.submit{width:115px;height:32px;flex:none;line-height:32px;background:var(--green);color:var(--white);font-size:13px;font-weight:700;text-align:center;text-transform:uppercase}

/* footer */
.site-footer{height:263px;background:var(--dark);color:var(--footer-text);font-size:12px;position:relative}
.footer-col{position:absolute;top:24px}
.footer-col h4{font-family:var(--head);font-weight:400;font-size:19px;color:#4a4a4a;text-transform:uppercase;margin-bottom:8px}
.col-links{left:132px}
.col-links li{position:relative;padding-left:14px;line-height:22px}
.col-links li::before{content:"";position:absolute;left:0;top:9px;width:6px;height:6px;border-radius:50%;background:var(--green)}
.col-about{left:292px;width:537px;line-height:1.6}
.col-about p{margin-bottom:14px}
.col-contact{left:852px;width:216px}
.footer-brand{font-family:var(--head);font-weight:700;font-size:30px;letter-spacing:2px;color:var(--white);display:flex;align-items:center;gap:8px;margin-bottom:14px}
.contact-list li{display:flex;gap:12px;line-height:1.5;margin-bottom:9px}
.contact-list svg{flex:none;margin-top:2px}
.col-contact .social{margin-top:14px;gap:6px}
.col-contact .social span{width:25px;height:25px;background:#e5e5e5}
.copyright{height:61px;background:var(--darker);color:#888;font-size:11px;text-align:center;line-height:61px}
</style>
</head>
<body>

<header class="site-header">
  <div class="brand"><span class="brand-dot"></span>VORMACE</div>
  <div class="topbar">
    <svg width="13" height="13" viewBox="0 0 24 24"><path fill="#f7931e" d="M6.6 10.8a15 15 0 0 0 6.6 6.6l2.2-2.2a1 1 0 0 1 1-.25 11.4 11.4 0 0 0 3.6.57 1 1 0 0 1 1 1V20a1 1 0 0 1-1 1A17 17 0 0 1 3 4a1 1 0 0 1 1-1h3.5a1 1 0 0 1 1 1c0 1.250.2 2.45.57 3.57a1 1 0 0 1-.25 1z"/></svg>
    <span>+ 1 555 014 9012</span>
    <div class="social"><span></span><span></span><span></span><span></span></div>
  </div>
  <nav class="main-nav"><span>Home</span><span>About Us</span><span>News</span><span>Contact Us</span></nav>
</header>

<section class="hero">
  <div class="hero-photo" role="img" aria-label="Yellow haul trucks driving along an open-pit mine road"></div>
  <h1 class="hero-title"><span class="l1">The Leader in Mining</span><span class="l2">Compnay in the World</span></h1>
  <span class="btn">Learn More</span>
  <div class="dots"><span></span><span></span><span></span></div>
</section>

<section class="welcome">
  <div class="wrap">
    <div class="section-head">
      <h2>Welcome to Our Company</h2>
      <p>Lorem ipsum dolor sit amet consectetur adipiscing elit</p>
    </div>
    <div class="welcome-body">
      <div class="welcome-photo" role="img" aria-label="Processing plant lit up at night"></div>
      <div class="welcome-text">
        <p>Lorem ipsum dolor sit amet, consectetur adipiscing elit. Vestibulum malesuada sagittis ultricies. Ut ut tempor velit. Sed non dolor et turpis semper consectetur.</p>
        <p>Interdum et malesuada fames ac ante ipsum primis in faucibus. Quisque convallis nec justo sed luctus. Praesent vulputate sed magna ac bibendum. Sed vehicula eu elit vitae eleifend. Morbi fermentum vel tortor ut sodales.</p>
        <ul class="bullets">
          <li>Vestibulum ante ipsum primis in faucibus orci luctus et</li>
          <li>Ultrices posuere cubilia curae nulla ut egestas velit</li>
          <li>Aenean ut quam lacinia tincidunt ex a molestie ex</li>
          <li>Praesent ut sodales massa id euismod dui</li>
          <li>Mauris dictum est sed urna cursus tincidunt</li>
        </ul>
      </div>
    </div>
  </div>
</section>

<div class="services-head section-head">
  <h2>Our Services</h2>
  <p>Lorem ipsum dolor sit amet consectetur adipiscing elit</p>
</div>
<section class="services">
  <div class="wrap service-cards">
    <article class="service-card">
      <div class="service-photo photo-mining" role="img" aria-label="Bucket-wheel excavator in an underground mine"></div>
      <h3>Mining</h3>
      <p>Lorem ipsum dolor sit amet consectetur adipiscing elit vestibulum malesuad anon.</p>
      <span class="btn">Read More</span>
    </article>
    <article class="service-card">
      <div class="service-photo photo-oil" role="img" aria-label="Oil tanker moored at a port"></div>
      <h3>Oil</h3>
      <p>Lorem ipsum dolor sit amet consectetur adipiscing elit vestibulum malesuad anon.</p>
      <span class="btn">Read More</span>
    </article>
    <article class="service-card">
      <div class="service-photo photo-gas" role="img" aria-label="Gas processing pipes and tanks under a blue sky"></div>
      <h3>Gas</h3>
      <p>Lorem ipsum dolor sit amet consectetur adipiscing elit vestibulum malesuad anon.</p>
      <span class="btn">Read More</span>
    </article>
  </div>
</section>

<section class="news">
  <div class="wrap">
    <div class="section-head">
      <h2>Latest News</h2>
      <p>The latest news, announcements &amp; activities at Vormace</p>
    </div>
    <div class="news-grid">
      <article class="news-card">
        <div class="news-photo photo-rig" role="img" aria-label="Offshore drilling platform at sea"></div>
        <div class="news-date">DEC<b>29</b>2014</div>
        <div class="news-body">
          <h3>Lorem ipsum dolor sit amet consectetur adipiscing</h3>
          <div class="news-meta">Posted by Dana Holt</div>
          <p class="excerpt">Lorem ipsum dolor sit amet, consectetur adipiscing elit. Vestibulum malesuada sagittis ultricies. Ut ut tempor velit. Sed non dolor et turpis.</p>
        </div>
        <div class="share"><span></span><span></span><span></span></div>
        <span class="read-more">Read Full Story</span>
      </article>
      <article class="news-card">
        <div class="news-photo photo-worker" role="img" aria-label="Worker in protective gear at an industrial site"></div>
        <div class="news-date">DEC<b>28</b>2014</div>
        <div class="news-body">
          <h3>Aliquam leo leo, mollis at aug uedictum fermentum libero</h3>
          <div class="news-meta">Posted by Dana Holt</div>
          <p class="excerpt">Lorem ipsum dolor sit amet conse ctetur adipiscing elit. Vestibulum male suada sagittis ultricies. Ut ut tem por velit. Sed non dolor et turpis.</p>
        </div>
        <div class="share"><span></span><span></span><span></span></div>
        <span class="read-more">Read Full Story</span>
      </article>
    </div>
    <span class="btn view-all">View All News and Events</span>
  </div>
</section>

<section class="newsletter">
  <div class="wrap">
    <div class="newsletter-copy">
      <h2>Signup <em>for</em> our <b>Monthly Newsletter</b></h2>
      <p>Lorem ipsum dolor sit amet consectetur adipiscing</p>
    </div>
    <div class="field">Enter Your Name</div>
    <div class="field">Enter Your Email</div>
    <div class="submit">Submit</div>
  </div>
</section>

<footer class="site-footer">
  <div class="footer-col col-links">
    <h4>Quick Links</h4>
    <ul><li>Home</li><li>About Us</li><li>Latest News</li><li>Contact Us</li></ul>
  </div>
  <div class="footer-col col-about">
    <h4>About Us</h4>
    <p>Lorem ipsum dolor sit amet consectetur adipiscing elit. Vestibulum malesuada sagittis ultricies. Ut ut tempor velit. Sed non dolor et turpis semper consectetur.</p>
    <p>Interdum et malesuada fames ac ante ipsum primis in faucibus. Quisque convallis nec justo sed luctus. Praesent vulputate sed magna ac bibendum. Lorem ipsum dolor sit amet consectetur adipiscing elit. Vestibulum malesuada sagittis ultricies. Ut ut tempor velit. Sed non dolor et turpis semper consectetur. Interdum et malesuada fames ac ante ipsum primis in faucibus.</p>
  </div>
  <div class="footer-col col-contact">
    <h4>Contact Us</h4>
    <div class="footer-brand"><span class="brand-dot"></span>VORMACE</div>
    <ul class="contact-list">
      <li><svg width="12" height="14" viewBox="0 0 24 28"><path fill="#f7931e" d="M12 0a10 10 0 0 0-10 10c0 7.5 10 18 10 18s10-10.5 10-18A10 10 0 0 0 12 0zm0 14a4 4 0 1 1 0-8 4 4 0 0 1 0 8z"/></svg><span>418 Ridgeline Road<br>Calder, TX 75001</span></li>
      <li><svg width="13" height="13" viewBox="0 0 24 24"><path fill="#f7931e" d="M6.6 10.8a15 15 0 0 0 6.6 6.6l2.2-2.2a1 1 0 0 1 1-.25 11.4 11.4 0 0 0 3.6.57 1 1 0 0 1 1 1V20a1 1 0 0 1-1 1A17 17 0 0 1 3 4a1 1 0 0 1 1-1h3.5a1 1 0 0 1 1 1c0 1.25.2 2.45.57 3.57a1 1 0 0 1-.25 1z"/></svg><span>+1-555-010-7890</span></li>
      <li><svg width="14" height="11" viewBox="0 0 24 18"><path fill="#f7931e" d="M0 0h24v18H0z"/><path fill="none" stroke="#353535" stroke-width="2" d="M1 1l11 9 11-9"/></svg><span>info@vormace-energy.com</span></li>
    </ul>
    <div class="social"><span></span><span></span><span></span><span></span></div>
  </div>
</footer>
<div class="copyright">Copyright © 2014 Vormace. All Rights Reserved. Privacy Policy &nbsp;|&nbsp; Sitemap</div>

</body>
</html>
```